Verdant Harvest Collective - Business Card Design Project

We need business cards for our business. We grow roots and fruits in Central and South America, we import and distribute in FL, USA. We do fresh and frozen products.

Target Market(s)

Small and big supermarkets, wholesalers, traders, distributors, etc

Industry/Entity Type

Business

```html
<!DOCTYPE html>
<html lang="en">
<head>
<meta charset="utf-8">
<title>Verdant Harvest Collective – Business Card</title>
<link href="https://fonts.googleapis.com/css2?family=Open+Sans:wght@400;600;700&display=swap" rel="stylesheet">
<style>
  :root {
    --backdrop: #e9e7e3;
    --card-white: #ffffff;
    --card-white-shade: #f1f1f1;
    --accent-orange: #e9a52c;
    --slate-dark: #3b3b3b;
    --slate-light: #6a6a6a;
    --ink-white: #ffffff;
    --ink-soft: #e4e4e4;
    --brand-gold: #e59a1f;
  }
  * { margin: 0; padding: 0; box-sizing: border-box; }
  html, body {
    width: 1200px;
    height: 886px;
    overflow: hidden;
    background: var(--backdrop);
    font-family: "Open Sans", Arial, sans-serif;
  }
  .stage {
    position: relative;
    width: 1200px;
    height: 886px;
    display: flex;
    align-items: center;
    justify-content: center;
  }
  .business-card {
    position: relative;
    width: 900px;
    height: 514px;
    border-radius: 22px;
    overflow: hidden;
    background: linear-gradient(180deg, var(--card-white) 0%, var(--card-white-shade) 100%);
    box-shadow: 0 10px 30px rgba(0,0,0,0.18);
  }
  .brand-area {
    position: absolute;
    top: 0; left: 0; right: 0;
    height: 214px;
    display: flex;
    align-items: center;
    justify-content: center;
    gap: 18px;
  }
  .brand-dot {
    width: 22px;
    height: 22px;
    border-radius: 50%;
    background: var(--brand-gold);
  }
  .brand-name {
    font-weight: 600;
    font-size: 50px;
    letter-spacing: 1px;
    color: var(--brand-gold);
    text-transform: uppercase;
  }
  .tagline-band {
    position: absolute;
    top: 214px; left: 0; right: 0;
    height: 32px;
    background: var(--accent-orange);
    display: flex;
    align-items: center;
    justify-content: center;
  }
  .tagline {
    color: var(--ink-white);
    font-weight: 600;
    font-size: 19px;
    letter-spacing: 0.2px;
  }
  .info-panel {
    position: absolute;
    top: 246px; left: 0; right: 0; bottom: 0;
    background: linear-gradient(90deg, var(--slate-dark) 0%, var(--slate-light) 60%, var(--slate-dark) 100%);
    display: flex;
    flex-direction: column;
    align-items: center;
    padding-top: 48px;
    text-align: center;
  }
  .person-name {
    color: var(--ink-white);
    font-weight: 700;
    font-size: 26px;
    letter-spacing: 0.5px;
    text-transform: uppercase;
    line-height: 1.1;
  }
  .person-title {
    color: var(--ink-soft);
    font-size: 15px;
    margin-top: 2px;
  }
  .service-summary {
    color: var(--ink-white);
    font-size: 28px;
    line-height: 1.25;
    margin-top: 34px;
  }
</style>
</head>
<body>
  <main class="stage">
    <section class="business-card" aria-label="Verdant Harvest Collective business card">
      <header class="brand-area">
        <span class="brand-dot" aria-hidden="true"></span>
        <span class="brand-name">Verdant Harvest Collective</span>
      </header>
      <div class="tagline-band">
        <p class="tagline">We grow roots and fruits in Central and South America</p>
      </div>
      <div class="info-panel">
        <p class="person-name">Marisol Reyes</p>
        <p class="person-title">Managing Director</p>
        <p class="service-summary">We do fresh and frozen products<br>we import and distribute in FL, USA</p>
      </div>
    </section>
  </main>
</body>
</html>
```